Business Card Design

Company is a Commercial Building Company specialising in New Construction and existing refurbishments

Industry/Entity Type

Business

Contact Information for Business Card

Dale Mercer
Construction Manager
E Dale@harbridgebuilding.com.au
M 0400 213 947
Mail 27 Tarrant Rise Brookhaven WA 6215

```html
<!DOCTYPE html>
<html lang="en">
<head>
<meta charset="utf-8">
<title>Harbridge Building &amp; Construction – Business Card</title>
<link rel="stylesheet" href="https://fonts.googleapis.com/css2?family=Exo+2:wght@400;600;700&display=swap">
<style>
  :root {
    --backdrop: #ececec;
    --card: #1b1a19;
    --cyan: #1cb3d6;
    --orange: #f5921e;
    --ink-light: #e9e9e9;
    --ink-soft: #cfcfcf;
  }
  * { box-sizing: border-box; margin: 0; padding: 0; }
  html, body {
    width: 1200px;
    height: 973px;
    overflow: hidden;
    background: var(--backdrop);
    font-family: "Exo 2", Arial, sans-serif;
  }
  .canvas {
    position: relative;
    width: 1200px;
    height: 973px;
  }
  .card {
    position: absolute;
    width: 640px;
    height: 390px;
    background: var(--card);
    box-shadow: 0 10px 28px rgba(0,0,0,0.18);
  }
  .card--front { left: 70px; top: 70px; }
  .card--back { left: 490px; top: 513px; }

  .brand {
    display: flex;
    align-items: center;
    gap: 16px;
  }
  .brand__mark {
    width: 26px;
    height: 26px;
    background: var(--orange);
    flex: none;
  }
  .brand__name {
    color: var(--ink-light);
    font-weight: 700;
    text-transform: uppercase;
    line-height: 1.05;
    letter-spacing: 0.5px;
    white-space: nowrap;
  }

  .card--front .brand {
    position: absolute;
    left: 0; right: 0; top: 0; bottom: 0;
    justify-content: center;
  }
  .card--front .brand__mark { width: 40px; height: 40px; }
  .card--front .brand__name { font-size: 40px; }

  .card--back .brand {
    position: absolute;
    left: 44px;
    top: 150px;
  }
  .card--back .brand__mark { width: 24px; height: 24px; }
  .card--back .brand__name { font-size: 22px; }

  .contact {
    position: absolute;
    left: 372px;
    top: 112px;
    width: 252px;
  }
  .contact__name {
    color: var(--cyan);
    font-weight: 700;
    font-size: 20px;
    text-transform: uppercase;
    letter-spacing: 0.5px;
  }
  .contact__role {
    color: var(--cyan);
    font-size: 16px;
    margin-bottom: 18px;
  }
  .contact__list { list-style: none; }
  .contact__item {
    display: flex;
    align-items: flex-start;
    gap: 10px;
    color: var(--ink-soft);
    font-size: 14.5px;
    line-height: 1.35;
    margin-bottom: 10px;
    white-space: nowrap;
  }
  .contact__icon {
    width: 16px;
    height: 16px;
    flex: none;
    margin-top: 2px;
  }
</style>
</head>
<body>
<main class="canvas">

  <section class="card card--front" aria-label="Card front">
    <div class="brand">
      <span class="brand__mark" aria-hidden="true"></span>
      <span class="brand__name">Harbridge Building<br>&amp; Construction</span>
    </div>
  </section>

  <section class="card card--back" aria-label="Card back">
    <div class="brand">
      <span class="brand__mark" aria-hidden="true"></span>
      <span class="brand__name">Harbridge Building<br>&amp; Construction</span>
    </div>

    <div class="contact">
      <p class="contact__name">Dale Mercer</p>
      <p class="contact__role">Construction Manager</p>
      <ul class="contact__list">
        <li class="contact__item">
          <svg class="contact__icon" viewBox="0 0 16 16" aria-hidden="true">
            <circle cx="8" cy="8" r="8" fill="var(--orange)"/>
            <rect x="5.5" y="3.5" width="5" height="9" rx="1" fill="none" stroke="#1b1a19" stroke-width="1.3"/>
          </svg>
          <span>0400 213 947</span>
        </li>
        <li class="contact__item">
          <svg class="contact__icon" viewBox="0 0 16 16" aria-hidden="true">
            <circle cx="8" cy="8" r="8" fill="var(--orange)"/>
            <rect x="4" y="5" width="8" height="6" fill="none" stroke="#1b1a19" stroke-width="1.2"/>
            <path d="M4 5 L8 8.5 L12 5" fill="none" stroke="#1b1a19" stroke-width="1.2"/>
          </svg>
          <span>Dale@harbridgebuilding.com.au</span>
        </li>
        <li class="contact__item">
          <svg class="contact__icon" viewBox="0 0 16 16" aria-hidden="true">
            <circle cx="8" cy="8" r="8" fill="var(--orange)"/>
            <path d="M8 13 C5.5 10 5 8.5 5 7 A3 3 0 0 1 11 7 C11 8.5 10.5 10 8 13 Z" fill="#1b1a19"/>
            <circle cx="8" cy="7" r="1.1" fill="var(--orange)"/>
          </svg>
          <span>27 Tarrant Rise<br>Brookhaven WA 6215</span>
        </li>
      </ul>
    </div>
  </section>

</main>
</body>
</html>
```